Emergency Medical Training and Events Company Business Needs Business Card Design

We are in need of a business card for our dynamic company expanding its customer base and need to be easily contacted and identified for when we visit with government officials, potential EMS / Fire agencies and county coordinators to arrange for training programs for first responders to better prepare them for critical thinking at critical incidents.

Target Market(s)

EMS/Fire and Event Promoters

Industry/Entity Type

Medical

Contact Information for Business Card

Two cards, comparable designs:

Martin K. Halvey, Principal, m.halvey@rvqtlo.com
Owen Tash, Event and Training Specialist, o.tash@rvqtlo.com

Font styles to use
Other font styles liked:
• Cambria

Colors

Designer to choose colors to be used in the design.

Requirements
Must have
• Company Logo, Spots for Name, Title, Phone Number, Email, Website
• A bullet list stating that we offer, QRB CPR and First Aid Instructors, Hold the Line Instructors, Event EMS, CME's, MCI Training and Planning. We prefer to have a black background for the card but if you can make a blue or white card stand out we would review that as well.
Should not have
• Tacky logos or special sayings ... simple, elegant, professional is the look we seek

```html
<!DOCTYPE html>
<html lang="en">
<head>
<meta charset="utf-8">
<title>RVQT Solutions – Business Cards</title>
<link href="https://fonts.googleapis.com/css2?family=Caladea:wght@400;700&display=swap" rel="stylesheet">
<style>
  :root {
    --backdrop: #48494c;
    --navy: #2e3682;
    --navy-deep: #262d72;
    --paper: #e6e7ea;
    --ink: #2e3682;
    --white: #ffffff;
    --faint: rgba(255,255,255,0.10);
  }
  * { box-sizing: border-box; margin: 0; padding: 0; }
  html, body {
    width: 1200px; height: 1190px; overflow: hidden;
    background: var(--backdrop);
    font-family: "Caladea", Cambria, Georgia, serif;
  }
  .card-sheet {
    position: relative; width: 1200px; height: 1190px;
  }
  .card {
    position: absolute; width: 520px; height: 300px;
    border-radius: 4px; overflow: hidden;
    box-shadow: 0 18px 30px rgba(0,0,0,0.45);
  }
  .card--front-a { left: 60px;  top: 200px; }
  .card--back-a  { left: 620px; top: 200px; }
  .card--back-b  { left: 60px;  top: 660px; }
  .card--front-b { left: 620px; top: 660px; }

  /* Front */
  .card-front {
    background: linear-gradient(160deg, var(--navy) 0%, var(--navy-deep) 100%);
    color: var(--white);
  }
  .card-front .faint-mark {
    position: absolute; left: -90px; top: -40px;
    width: 300px; height: 300px; border-radius: 50%;
    background: var(--faint);
  }
  .brand {
    display: flex; align-items: center; gap: 10px;
  }
  .brand-dot {
    width: 34px; height: 34px; border-radius: 50%;
    background: var(--white); flex: none;
  }
  .brand-name {
    font-weight: 700; font-size: 30px; letter-spacing: 1px;
    color: var(--white); line-height: 1;
  }
  .card-front .brand { position: absolute; left: 190px; top: 72px; }
  .service-list {
    position: absolute; left: 190px; top: 128px;
    list-style: none; font-size: 14.5px; line-height: 1.55;
  }
  .service-list li { display: flex; align-items: center; gap: 8px; }
  .service-list li::before {
    content: ""; width: 7px; height: 7px; border-radius: 50%;
    border: 1.5px solid var(--white); flex: none;
  }

  /* Back */
  .card-back { background: var(--paper); color: var(--ink); }
  .card-back .wave-panel {
    position: absolute; inset: 0; width: 520px; height: 300px;
  }
  .card-back .brand {
    position: absolute; right: 26px; top: 128px;
  }
  .card-back .brand-dot { width: 24px; height: 24px; }
  .card-back .brand-name { font-size: 21px; }
  .person {
    position: absolute; left: 34px; top: 56px;
  }
  .person-name { font-size: 30px; font-weight: 400; line-height: 1.05; }
  .person-title {
    font-size: 13px; letter-spacing: 1.5px; text-transform: uppercase;
    margin-top: 4px; line-height: 1.2;
  }
  .contact {
    position: absolute; left: 34px; bottom: 42px;
    list-style: none; font-size: 15px; line-height: 1.55;
  }
</style>
</head>
<body>
<main class="card-sheet">

  <section class="card card-front card--front-a">
    <div class="faint-mark"></div>
    <div class="brand"><span class="brand-dot"></span><span class="brand-name">RVQT Solutions</span></div>
    <ul class="service-list">
      <li>QRB CPR and First Aid Instructors.</li>
      <li>Hold the Line Instructors.</li>
      <li>EMS CMEs, MCI Training and Planning</li>
    </ul>
  </section>

  <section class="card card-back card--back-a">
    <svg class="wave-panel" viewBox="0 0 520 300" aria-hidden="true">
      <path fill="var(--navy)" d="M345 0 C305 30 335 62 312 92 C290 122 332 150 306 182 C284 214 330 242 314 270 C308 284 318 294 326 300 H520 V0 Z"/>
    </svg>
    <div class="brand"><span class="brand-dot"></span><span class="brand-name">RVQT Solutions</span></div>
    <div class="person">
      <h2 class="person-name">Martin K. Halvey</h2>
      <p class="person-title">Principal</p>
    </div>
    <ul class="contact">
      <li>555.201.4730</li>
      <li>www.rvqtlo.com</li>
      <li>m.halvey@rvqtlo.com</li>
    </ul>
  </section>

  <section class="card card-back card--back-b">
    <svg class="wave-panel" viewBox="0 0 520 300" aria-hidden="true">
      <path fill="var(--navy)" d="M345 0 C305 30 335 62 312 92 C290 122 332 150 306 182 C284 214 330 242 314 270 C308 284 318 294 326 300 H520 V0 Z"/>
    </svg>
    <div class="brand"><span class="brand-dot"></span><span class="brand-name">RVQT Solutions</span></div>
    <div class="person">
      <h2 class="person-name">Owen Tash</h2>
      <p class="person-title">Event and Training<br>Specialist</p>
    </div>
    <ul class="contact">
      <li>555.201.4731</li>
      <li>www.rvqtlo.com</li>
      <li>o.tash@rvqtlo.com</li>
    </ul>
  </section>

  <section class="card card-front card--front-b">
    <div class="faint-mark"></div>
    <div class="brand"><span class="brand-dot"></span><span class="brand-name">RVQT Solutions</span></div>
    <ul class="service-list">
      <li>QRB CPR and First Aid Instructors.</li>
      <li>Hold the Line Instructors.</li>
      <li>EMS CMEs, MCI Training and Planning</li>
    </ul>
  </section>

</main>
</body>
</html>
```